Re design current site.

Redesign of the current site. Like current design But I don't own it so I need a custom design similar to the current one. Want the model pictures to be shown off as they currently do on the home page I want to show off contact info make it very noticeable and readable.
Target Market(s)
Males age 30-60
Number of Pages Required
1 page
Requirements
Must have
- Must show off model pictures on the page. Must show contact info easy to read easy to find.

```html
<!DOCTYPE html>
<html lang="en">
<head>
<meta charset="utf-8">
<title>Velour Models</title>
<link rel="stylesheet" href="https://fonts.googleapis.com/css2?family=Playfair+Display:ital,wght@0,400;0,700;1,400&family=Work+Sans:wght@400;500;600&display=swap">
<style>
:root{
  --ink:#1c1c1c;
  --night:#141414;
  --coal:#232323;
  --red:#e3202d;
  --paper:#f4f4f4;
  --white:#ffffff;
  --grey:#6d6d6d;
  --line:#e2e2e2;
}
*{box-sizing:border-box;margin:0;padding:0}
html,body{width:1200px;height:4045px;overflow:hidden}
body{position:relative;font-family:"Work Sans",sans-serif;color:var(--ink);background:var(--white)}
section,footer{position:absolute;left:0;width:1200px;overflow:hidden}
.abs{position:absolute}
.center{left:0;width:1200px;text-align:center}

/* hero */
.hero{top:0;height:588px;background:radial-gradient(circle at 80% 20%,#2d2d2d 0,#1d1d1d 45%,#121212 100%)}
.hero-deco{position:absolute;border-radius:50%;background:rgba(255,255,255,.035)}
.brand{position:absolute;top:32px;left:0;width:1200px;display:flex;justify-content:center;align-items:center;gap:14px}
.brand-mark{width:34px;height:34px;background:var(--white)}
.brand-name{font-weight:600;font-size:44px;letter-spacing:1px;color:var(--white)}
.menu{position:absolute;top:48px;right:80px;width:22px}
.menu span{display:block;height:3px;background:var(--white);margin-bottom:5px}
.hero-site{top:252px;font-size:15px;color:var(--white)}
.hero-site b{color:var(--red);font-weight:500}
.hero-title{top:284px;font-family:"Playfair Display",serif;font-style:italic;font-weight:400;font-size:42px;line-height:54px;color:var(--white);letter-spacing:2px}
.hero-down{top:488px;left:578px;width:44px;height:44px;border:1px solid #777;border-radius:50%}

/* about */
.about{top:588px;height:369px;background:var(--paper)}
.h2{font-family:"Playfair Display",serif;font-size:32px;color:var(--ink)}
.about .h2{top:78px;font-weight:400}
.about p{top:137px;left:140px;width:920px;text-align:center;font-size:13px;line-height:20px;color:#444}
.btn{display:block;background:var(--red);color:var(--white);font-size:13px;letter-spacing:.5px;text-align:center}
.about .btn{top:256px;left:492px;width:216px;height:54px;line-height:54px}

/* contact band */
.band{top:957px;height:230px;background:repeating-linear-gradient(45deg,#1b1b1b 0 6px,#222 6px 12px)}
.band-item{top:100px;color:var(--white);font-size:13px;line-height:18px}
.band-item b{display:block;font-weight:500}
.band-msg{top:70px;font-size:15px;line-height:26px;letter-spacing:1px;color:var(--white);font-weight:500}
.band-note{top:135px;font-size:11px;letter-spacing:1px;color:var(--red)}

/* models */
.models{top:1187px;height:1267px;background:var(--white)}
.models .h2{top:68px;font-weight:700}
.models .sub{top:130px;left:300px;width:600px;text-align:center;font-size:13px;line-height:20px;color:#444}
.tile{position:absolute;width:326px}
.view{display:flex;flex-direction:column;align-items:center;justify-content:center;background:#f7f7f7}
.view strong{font-family:"Playfair Display",serif;font-size:22px;letter-spacing:1px}
.view small{color:var(--red);font-size:11px;margin-top:6px;letter-spacing:1px}

/* why */
.why{top:2454px;height:440px;background:linear-gradient(#1f1f1f,#161616)}
.why .h2{top:50px;color:var(--white);font-weight:700}
.why .h2 b{color:var(--red);font-weight:700}
.why p{top:145px;left:280px;width:640px;text-align:center;font-family:"Playfair Display",serif;font-style:italic;font-size:16px;line-height:32px;color:var(--white)}
.dots{top:383px;display:flex;justify-content:center;gap:10px}
.dots i{width:7px;height:7px;border-radius:50%;background:#666}
.dots i.on{background:var(--white)}

/* badge strip */
.trust{top:2894px;height:175px;background:var(--white)}
.badge{left:221px;top:27px;width:132px;height:120px;background:#d8d3bd;border:3px solid #b5ad8d}
.trust p{left:391px;top:45px;width:600px;font-family:"Playfair Display",serif;font-size:17px;line-height:28px;color:var(--ink)}

/* contact */
.contact{top:3069px;height:551px;background:var(--paper)}
.contact h3{left:86px;top:88px;font-family:"Playfair Display",serif;font-weight:700;font-size:36px;color:var(--red)}
.contact .intro{left:86px;top:156px;width:385px;font-size:13.5px;line-height:22px;color:#333}
.info{left:86px;font-size:13.5px;color:#333}
.info b{color:var(--red);font-weight:500}
.field{position:absolute;background:var(--white);color:#999;font-size:12px;padding:0 18px;line-height:46px}
.contact .btn{left:523px;top:418px;width:160px;height:48px;line-height:48px}

/* footer */
.foot{top:3620px;height:425px;background:var(--night);color:var(--white)}
.foot h4{font-family:"Playfair Display",serif;font-weight:700;font-size:19px}
.foot-mark{left:0;top:0;width:70px;height:70px;border-right:3px solid var(--red);border-bottom:3px solid var(--red)}
.foot .about-text{left:86px;top:118px;width:300px;font-size:13px;line-height:22px;font-weight:500}
.links{display:grid;grid-template-columns:150px 150px;row-gap:34px;font-size:12px;letter-spacing:1px}
.links span::before{content:"›  ";color:var(--red)}
.news{left:790px;top:130px;width:318px;height:44px;background:var(--white);color:#999;font-size:12px;padding-left:16px;line-height:44px}
.foot .btn{left:790px;top:184px;width:318px;height:44px;line-height:44px;font-size:16px;font-family:"Playfair Display",serif}
.copy{left:0;top:372px;width:1200px;height:53px;line-height:53px;border-top:1px solid #2a2a2a;text-align:center;font-size:12px;color:#ccc}
</style>
</head>
<body>

<section class="hero">
  <div class="hero-deco" style="left:-90px;top:-40px;width:380px;height:380px"></div>
  <div class="hero-deco" style="left:870px;top:60px;width:300px;height:300px"></div>
  <div class="hero-deco" style="left:600px;top:420px;width:420px;height:420px"></div>
  <div class="brand"><span class="brand-mark"></span><span class="brand-name">VELOUR MODELS</span></div>
  <div class="menu"><span></span><span></span><span></span></div>
  <div class="abs center hero-site">Velour<b>Models</b>.com</div>
  <h1 class="abs center hero-title">TREAT YOURSELF<br>AND WE'LL TREAT YOU</h1>
  <div class="abs hero-down">
    <svg width="44" height="44" viewBox="0 0 44 44"><path d="M18 20l4 4 4-4" fill="none" stroke="#aaa" stroke-width="1.5"/></svg>
  </div>
</section>

<section class="about">
  <h2 class="abs center h2">About Our Agency</h2>
  <p class="abs">VelourModels Concierge Service allows clients to request VelourModels to search for models in the location you plan on traveling to.<br>We will search and find attractive models for the dates requested. We also verify they are interested in the service you expect/request and that the pictures we have are recent and real.</p>
  <a class="abs btn">BOOK A MODEL NOW</a>
</section>

<section class="band">
  <svg class="abs" style="left:86px;top:100px" width="36" height="36" viewBox="0 0 24 24"><path fill="#fff" d="M6.6 10.8a15 15 0 006.6 6.6l2.2-2.2c.3-.3.7-.4 1-.2 1.1.4 2.3.6 3.6.6.6 0 1 .4 1 1V20c0 .6-.4 1-1 1A17 17 0 013 4c0-.6.4-1 1-1h3.5c.6 0 1 .4 1 1 0 1.3.2 2.5.6 3.6.1.3 0 .7-.2 1z"/></svg>
  <div class="abs band-item" style="left:140px"><b>PHONE</b>555-014-2287</div>
  <div class="abs center band-msg">PLEASE CONTACT US ABOUT ADDITIONAL MODELS<br>NOT POSTED PUBLICLY!</div>
  <div class="abs center band-note">MALE &amp; FEMALE COUPLE AVAILABLE AS WELL</div>
  <div class="abs band-item" style="right:150px;text-align:right"><b>EMAIL</b>HELLO@VELOURMODELS.COM</div>
  <svg class="abs" style="left:1068px;top:102px" width="44" height="32" viewBox="0 0 44 32"><rect x="1.5" y="1.5" width="41" height="29" fill="none" stroke="#fff" stroke-width="2.5"/><path d="M2 2l20 16L42 2" fill="none" stroke="#fff" stroke-width="2.5"/></svg>
</section>

<section class="models">
  <h2 class="abs center h2">Our Models</h2>
  <p class="abs sub">Are you looking for the best Miami Model Services providing incall and outcall serving the Miami, Fort Lauderdale, West Palm Beach &amp; other major city's?</p>
  <div class="tile" role="img" aria-label="Model portrait photo" style="left:86px;top:224px;height:221px;background:linear-gradient(#caa5a2,#b2646d)"></div>
  <div class="tile" role="img" aria-label="Model portrait photo" style="left:86px;top:469px;height:221px;background:linear-gradient(#5b3a36,#c2263a)"></div>
  <div class="tile" role="img" aria-label="Model portrait photo" style="left:86px;top:714px;height:467px;background:linear-gradient(#6f6660,#3c3532)"></div>
  <div class="tile" role="img" aria-label="Model portrait photo" style="left:437px;top:224px;height:466px;background:linear-gradient(#8a6a5a,#c9a48f)"></div>
  <div class="tile view" style="left:437px;top:714px;height:221px"><strong>VIEW ALL MODELS</strong><small>CLICK HERE</small></div>
  <div class="tile" role="img" aria-label="Model portrait photo" style="left:437px;top:963px;height:218px;background:linear-gradient(#7c5a4c,#b38b78)"></div>
  <div class="tile" role="img" aria-label="Model portrait photo" style="left:790px;top:224px;height:221px;background:linear-gradient(#1b1513,#3a2b26)"></div>
  <div class="tile" role="img" aria-label="Model portrait photo" style="left:790px;top:469px;height:467px;background:linear-gradient(#5e7a4a,#a59a7f)"></div>
  <div class="tile" role="img" aria-label="Model portrait photo" style="left:790px;top:963px;height:218px;background:linear-gradient(#8f4a32,#c9b5a8)"></div>
</section>

<section class="why">
  <h2 class="abs center h2">Why <b>VelourModels</b>.com</h2>
  <p class="abs">At VelourModels, you will come across highly appealing, beautiful, and intelligent companions. Our South Florida Service portfolio of girls includes the towns best fashion models, hot college girls, girls next door, independent working women etc., to serve all the gentlemen with excellent standards.</p>
  <div class="abs center dots"><i></i><i class="on"></i><i></i></div>
</section>

<section class="trust">
  <div class="abs badge" role="img" aria-label="Certification badge"></div>
  <p class="abs">Reward yourself with a highly professional and attractive companion to admire and enjoy memorable moments in Miami, Fort Lauderdale and West Palm Beach!</p>
</section>

<section class="contact">
  <h3 class="abs">Contact Info:</h3>
  <p class="abs intro">Call Now and book a model 555-014-2287 or write us at hello@velourmodels.com with your requirement and we will make all arrangements to make your time memorable with our services! We guarantee that you will have some of the most beautiful, intelligent, &amp; alluring performers and entertainers at your place in no time to make your time memorable.</p>
  <div class="abs info" style="top:345px"><b>Address:</b>&nbsp; 418 Palmetto Avenue, FL</div>
  <div class="abs info" style="top:378px"><b>Phone:</b>&nbsp; +555-014-2287</div>
  <div class="abs info" style="top:411px"><b>Email:</b>&nbsp; hello@velourmodels.com</div>
  <div class="field" style="left:523px;top:102px;width:284px">Your Name</div>
  <div class="field" style="left:830px;top:102px;width:284px">Your Email</div>
  <div class="field" style="left:523px;top:170px;width:591px">Your Title</div>
  <div class="field" style="left:523px;top:238px;width:591px;height:150px">Your Comment</div>
  <a class="abs btn">SEND MESSAGE</a>
</section>

<footer class="foot">
  <div class="abs foot-mark"></div>
  <h4 class="abs" style="left:86px;top:80px">About Us</h4>
  <p class="abs about-text">we, at VelourModels, can accommodate your dreams &amp; demands for any and all kinds of engagements. Our main goal is to offer you a fully satisfying, warm, and pleasurable encounter that you will never forget!</p>
  <h4 class="abs" style="left:437px;top:80px">Quick Links</h4>
  <div class="abs links" style="left:437px;top:132px"><span>HOME</span><span>MODELS</span><span>BOOKINGS</span><span>EMPLOYMENT</span><span>RATES</span><span>LINKS</span></div>
  <h4 class="abs" style="left:790px;top:80px">Subscribe to our newsletter</h4>
  <div class="abs news">Your Email Address</div>
  <a class="abs btn">JOIN NOW</a>
  <div class="abs copy">© 2017. Copyright belongs to VelourModels.com</div>
</footer>

</body>
</html>
```